Harlow SMSO Covid-19 Vaccine Advertisement (Digital + Print)

The client is needing an advertisement that will run during Football and Soccer Season to advertise getting vaccinated for the Covid-19 Shot.
Request - Sports theme related, Scoreboard, Teams match up, covid-19 vs texas theme

Client - Harlow County Senior and Mobility Support Office

Various Ad types:
Digital Marketing Insertion Orders
- Door Hanger
- Front Page Note
- Insert Schedule

Print + Digital Insertion Orders
- Print Ads
- Email Marketing
- Banner Ads

Must include: logo and brand colors and 1-888-555-0147, and #RaiseTheBarQP and needs to be an English version and a Spanish Version

Message Ideas to incorporate - a variation - do not use all in one ad
Harlow vs COVID
Let’s win this together!
#VaccineSavesLives
#CancelCOVID
#GetVaccinated
#GetBoosted
#GetProtected

```html
<!DOCTYPE html>
<html lang="en">
<head>
<meta charset="utf-8">
<title>Harlow vs Covid – Vaccine Ad</title>
<link rel="stylesheet" href="https://fonts.googleapis.com/css2?family=Bebas+Neue&family=Roboto+Condensed:wght@400;700&family=Montserrat:wght@600&display=swap">
<style>
  :root {
    --night: #0d1733;
    --stadium-blue: #1f3f8f;
    --flame: #c4561f;
    --grass: #5f6b1f;
    --grass-dark: #0f2416;
    --board: #17224f;
    --board-edge: #0e1638;
    --text: #ffffff;
    --rule: rgba(255,255,255,0.6);
  }
  html, body {
    margin: 0;
    padding: 0;
    width: 1200px;
    height: 1200px;
    overflow: hidden;
    background: var(--night);
  }
  .ad {
    position: relative;
    width: 1200px;
    height: 1200px;
    overflow: hidden;
    color: var(--text);
    font-family: "Roboto Condensed", sans-serif;
  }
  .stadium-backdrop {
    position: absolute;
    inset: 0;
    background:
      radial-gradient(ellipse 420px 380px at 600px 560px, rgba(40,70,150,0.75), rgba(40,70,150,0) 70%),
      radial-gradient(ellipse 520px 260px at 600px 260px, rgba(196,86,31,0.55), rgba(196,86,31,0) 75%),
      linear-gradient(180deg, #13275e 0%, var(--night) 30%, #1c2a55 52%, var(--grass) 72%, var(--grass-dark) 100%);
  }
  .headline {
    position: absolute;
    top: 0;
    left: 0;
    width: 1200px;
    height: 0;
    font-family: "Bebas Neue", sans-serif;
  }
  .team {
    position: absolute;
    top: 118px;
    font-size: 112px;
    line-height: 1;
    letter-spacing: 2px;
    transform: translateX(-50%);
  }
  .team--home { left: 305px; }
  .team--away { left: 885px; }
  .versus {
    position: absolute;
    left: 610px;
    top: 78px;
    font-size: 190px;
    line-height: 1;
    transform: translateX(-50%);
  }
  .tagline {
    position: absolute;
    top: 318px;
    left: 0;
    width: 1190px;
    text-align: center;
    font-size: 52px;
    letter-spacing: -0.5px;
  }
  .scoreboard {
    position: absolute;
    top: 427px;
    width: 381px;
    height: 367px;
    background: var(--board-edge);
    border-radius: 8px;
    display: flex;
    gap: 14px;
    padding: 16px;
    box-sizing: border-box;
  }
  .scoreboard--home { left: 113px; }
  .scoreboard--away { left: 696px; }
  .score-digit {
    flex: 1;
    background: var(--board);
    border-radius: 6px;
    display: flex;
    align-items: center;
    justify-content: center;
    font-family: "Roboto Condensed", sans-serif;
    font-weight: 700;
    font-size: 300px;
    line-height: 1;
  }
  .brand {
    position: absolute;
    top: 872px;
    left: 0;
    width: 1190px;
    display: flex;
    justify-content: center;
    align-items: center;
    gap: 18px;
  }
  .brand-dot {
    width: 62px;
    height: 62px;
    border-radius: 50%;
    background: var(--text);
  }
  .brand-name {
    font-family: "Montserrat", sans-serif;
    font-weight: 600;
    font-size: 44px;
    letter-spacing: 1px;
  }
  .contact {
    position: absolute;
    top: 972px;
    left: 0;
    width: 1180px;
    text-align: center;
    font-size: 50px;
  }
  .divider {
    position: absolute;
    top: 1048px;
    left: 527px;
    width: 126px;
    height: 2px;
    background: var(--rule);
  }
  .hashtag {
    position: absolute;
    top: 1064px;
    left: 0;
    width: 1180px;
    text-align: center;
    font-size: 40px;
  }
</style>
</head>
<body>
  <main class="ad">
    <div class="stadium-backdrop" role="img" aria-label="Night stadium with blue floodlights, a flaming soccer ball at centre and a grass pitch below"></div>

    <h1 class="headline">
      <span class="team team--home">HARLOW</span>
      <span class="versus">VS</span>
      <span class="team team--away">COVID</span>
    </h1>

    <p class="tagline" style="margin:0">LET’S WIN THIS TOGETHER!</p>

    <div class="scoreboard scoreboard--home" aria-label="Harlow score 00">
      <span class="score-digit">0</span>
      <span class="score-digit">0</span>
    </div>
    <div class="scoreboard scoreboard--away" aria-label="Covid score 00">
      <span class="score-digit">0</span>
      <span class="score-digit">0</span>
    </div>

    <div class="brand">
      <span class="brand-dot"></span>
      <span class="brand-name">Harlow SMSO</span>
    </div>

    <p class="contact" style="margin:0">1-888-555-0147, &amp; #RAISETHEBARQP</p>
    <div class="divider"></div>
    <p class="hashtag" style="margin:0">#VaccineSavesLives</p>
  </main>
</body>
</html>
```